Brisk Meadow LLC business card

I created a front and back idea of what I want. Also I included my Brisk Meadow logo to be used on the card. Please use your creativity to make it look professional and awesome! Use the all text and phrases in the sample card that I made.

(Front of card)Key words and phrases:
FOOD GROWING MACHINES
Aeroponics Technology
No soil
No pesticides
98% less water
Grow year round

(Back of card)
EVERY MONTH ONE PILLAR PLOT WILL BE GIVEN AWAY
FOLLOW US ON IG FOR A CHANCE TO WIN A PILLAR PLOT
FOOD GROWING MACHINES
Vertical Farming
Urban Farming
100% Organic
Grows 40% Faster
Indoors/outdoors

My contact info:
Chef Rulo
Phone:415 372-8491
web: briskmeadow.example
IG: briskmeadowvx

Target Market(s)

urban farming, vertical farming gardening

Industry/Entity Type

Gardening

Contact Information for Business Card

Front of card)Key words and phrases:
FOOD GROWING MACHINES
Aeroponics Technology
No soil
No pesticides
98% less water
Grow year round

(Back of card)
FOOD GROWING MACHINES
Vertical Farming
Urban Farming
100% Organic
Grows 40% Faster
Indoors/outdoors

My contact info:
Phone:415 372-8491
web: briskmeadow.example
IG: briskmeadowvx

Requirements
Must have
• My contact info:
Chef Rulo
Phone:415 372-8491
web: briskmeadow.example
IG: briskmeadowvx
Nice to have
• Great imagery and easy to read. Try to incorporate the image that I uploaded of the little girl.

```html
<!DOCTYPE html>
<html lang="en">
<head>
<meta charset="utf-8">
<title>Brisk Meadow Business Card</title>
<link href="https://fonts.googleapis.com/css2?family=Ubuntu:wght@400;500;700&display=swap" rel="stylesheet">
<style>
  :root{
    --backdrop:#3b332d;
    --front-blue:#5a6db6;
    --brand-green:#8dc63f;
    --text-green:#5e9a2c;
    --deep-green:#3f6f24;
    --pale-green:#e6f2cc;
    --paper:#fbfdf5;
    --white:#ffffff;
  }
  *{box-sizing:border-box;margin:0;padding:0}
  html,body{width:1200px;height:1200px;overflow:hidden}
  body{background:var(--backdrop);font-family:"Ubuntu",sans-serif;position:relative}
  .card{position:absolute;left:128px;width:945px;height:540px;overflow:hidden;box-shadow:0 10px 24px rgba(0,0,0,.35)}
  .card-front{top:40px;background:var(--front-blue);color:var(--white)}
  .card-back{top:620px;background:radial-gradient(circle at 72% 48%,var(--paper) 0%,var(--pale-green) 80%);color:var(--text-green)}

  .brand{font-weight:700;color:var(--brand-green);text-transform:uppercase;line-height:.9;display:flex;align-items:center;gap:12px}
  .brand-dot{width:22px;height:22px;border-radius:50%;background:var(--brand-green);flex:none}

  .front-brand{position:absolute;left:80px;top:110px;font-size:62px}
  .front-brand .brand-dot{width:30px;height:30px;align-self:flex-start}
  .front-lines{position:absolute;left:100px;top:275px;font-size:21px;line-height:1.75;font-weight:500}
  .front-lines li{list-style:none}
  .front-lines li:nth-child(2){padding-left:18px}
  .front-lines li:nth-child(3){padding-left:36px}
  .front-lines li:nth-child(4){padding-left:54px}

  .sprout{position:absolute;border-radius:60% 40% 55% 45%}
  .front-sprout{right:70px;top:80px;width:300px;height:400px;background:radial-gradient(circle at 50% 40%,rgba(140,190,150,.75),rgba(110,160,140,.35) 70%,transparent 72%)}
  .back-sprout{right:60px;top:110px;width:340px;height:420px;background:radial-gradient(circle at 50% 40%,rgba(170,210,110,.85),rgba(190,225,140,.45) 68%,transparent 72%)}

  .back-brand{position:absolute;right:70px;top:56px;font-size:44px}
  .back-info{position:absolute;left:70px;top:150px;font-size:21px;font-weight:500;line-height:1.6}
  .contact{margin-top:14px;display:flex;flex-direction:column;gap:8px;font-size:24px}
  .contact-row{display:flex;align-items:center;gap:10px}
  .contact-row svg{flex:none}
  .service-title{margin-top:34px;font-size:26px;color:var(--deep-green);font-weight:500;letter-spacing:.5px;padding-bottom:8px;border-bottom:2px solid var(--brand-green);display:inline-block;padding-right:30px}
  .service-list{margin-top:12px;list-style:none;font-size:22px;line-height:1.7}
  .service-list li:nth-child(2){padding-left:20px}
  .service-list li:nth-child(3){padding-left:40px}
</style>
</head>
<body>
  <section class="card card-front" aria-label="Card front">
    <div class="sprout front-sprout" role="img" aria-label="Large translucent sprout with two leaves"></div>
    <div class="brand front-brand"><span>Brisk<br>Meadow</span><span class="brand-dot"></span></div>
    <ul class="front-lines">
      <li>FOOD GROWING MACHINES</li>
      <li>Aeroponics Technology</li>
      <li>No soil | No pesticides</li>
      <li>98% less water | Grow year round</li>
    </ul>
  </section>

  <section class="card card-back" aria-label="Card back">
    <div class="sprout back-sprout" role="img" aria-label="Soft green sprout with two leaves"></div>
    <div class="brand back-brand"><span>Brisk<br>Meadow</span><span class="brand-dot"></span></div>
    <div class="back-info">
      <p>Every Month One Pillar Plot Will Be Given Away</p>
      <p>Follow Us On Ig For A Chance To Win A Pillar Plot</p>
      <div class="contact">
        <div class="contact-row">
          <svg width="24" height="24" viewBox="0 0 24 24" aria-hidden="true"><circle cx="12" cy="12" r="10" fill="none" stroke="currentColor" stroke-width="2.2"/></svg>
          <span>briskmeadowvx</span>
        </div>
        <div class="contact-row">
          <svg width="24" height="24" viewBox="0 0 24 24" aria-hidden="true"><path d="M6.6 10.8a15.1 15.1 0 0 0 6.6 6.6l2.2-2.2a1 1 0 0 1 1-.25 11.4 11.4 0 0 0 3.6.57 1 1 0 0 1 1 1V20a1 1 0 0 1-1 1A17 17 0 0 1 3 4a1 1 0 0 1 1-1h3.5a1 1 0 0 1 1 1c0 1.25.2 2.45.57 3.57a1 1 0 0 1-.25 1z" fill="currentColor"/></svg>
          <span>415 372-8491 |</span>
          <svg width="22" height="22" viewBox="0 0 24 24" aria-hidden="true"><g fill="none" stroke="currentColor" stroke-width="1.8"><circle cx="12" cy="12" r="9.5"/><ellipse cx="12" cy="12" rx="4.2" ry="9.5"/><path d="M2.5 12h19"/></g></svg>
          <span>briskmeadow.example</span>
        </div>
      </div>
      <h2 class="service-title">OUR SERVICE</h2>
      <ul class="service-list">
        <li>Food Growing Machines | Vertical Farming</li>
        <li>Urban Farming | 100% Organic</li>
        <li>Grows 40% Faster | Indoors/outdoors</li>
      </ul>
    </div>
  </section>
</body>
</html>
```